Organic skincare label - minimalist, earthy, luxe design needed!

I need a label design for a luxury natural skin care line called "Velka Botanix". Velka means 'earth' in Swahili. I would like the design to embody an earthy feel but be minimalistic and give a luxe vibe. My first product will be a Tumeric and Neem Scrub.

The size of the jar is 8oz, label dimensions should be (1.625" Tall x 8.5" Wide)
I will be making other products too such as; oils + toners so I feel free to do labels for glass bottles and/or spray bottles as well.

Forest green, light pinks/nudes/beige, grey, white, gold, are colors that can be used (not all have to be used).

I have included pictures of some things I've worked on myself as well as my original logo design but I need to simplify the logo, no circle around it.
Feel free to get creative.

Thank you! :)
Updates

Target Market(s)

Socially Conscious, Beauty Enthusiast, Minimalist

Industry/Entity Type

Skin Care

Font styles to use
Sans Serif
Other font styles liked:
• "Wonderlove doodle" is the font used for "Velka" in the logo. Feel free to use that or change it as you see fit.

Requirements
Must have
• Simplistic design
would like to stick to a font close to the ones in the logo. Either the one used for the name "Velka" OR the one that the slogan "Nature's Rituals" uses.

I have also included some pictures to capture the aesthetic of my social media and website.

Gender neutral

```html
<!DOCTYPE html>
<html lang="en">
<head>
<meta charset="utf-8">
<title>Velka Botanix – Tumeric and Neem Scrub Label</title>
<link href="https://fonts.googleapis.com/css2?family=Montserrat:wght@500;600&display=swap" rel="stylesheet">
<style>
  :root {
    --page: #f6f6f6;
    --label-light: #e7dfd3;
    --label-mid: #cfc4b6;
    --label-dark: #a3978a;
    --ink: #2a2a2a;
    --rule: #1f1f1f;
  }
  * { box-sizing: border-box; margin: 0; padding: 0; }
  html, body {
    width: 1200px; height: 1200px; overflow: hidden;
    background: var(--page);
    font-family: "Montserrat", sans-serif;
    color: var(--ink);
  }
  .label {
    position: absolute;
    left: 50px; top: 397px;
    width: 1100px; height: 406px;
    background: linear-gradient(90deg, var(--label-light) 0%, var(--label-mid) 45%, var(--label-dark) 80%, var(--label-mid) 100%);
  }
  .rule { position: absolute; background: var(--rule); }
  .rule--top-left { left: 0; top: 22px; width: 321px; height: 3px; }
  .rule--top-right { left: 362px; top: 22px; right: 0; height: 3px; }
  .rule--bottom-thin { left: 0; right: 0; top: 374px; height: 2px; }
  .rule--bottom-thick { left: 0; right: 0; top: 390px; height: 4px; }

  .brand {
    position: absolute; left: 312px; width: 390px; top: 40px;
    text-align: center;
    font-weight: 500; font-size: 52px; line-height: 62px; letter-spacing: 1px;
    white-space: nowrap;
  }
  .slogan {
    position: absolute; left: 418px; width: 262px; top: 104px;
    text-align: center;
    font-weight: 600; font-size: 21px; line-height: 28px; letter-spacing: 2px;
    white-space: nowrap;
  }
  .product-name {
    position: absolute; left: 190px; width: 670px; top: 176px;
    text-align: center;
    font-weight: 600; font-size: 43px; line-height: 50px; letter-spacing: 2.5px;
    white-space: nowrap;
  }
  .product-rule {
    position: absolute; left: 219px; width: 612px; top: 236px; height: 1.5px;
    background: var(--rule);
  }
  .badges { position: absolute; left: 300px; top: 268px; }
  .details {
    position: absolute; left: 552px; top: 274px; width: 166px;
    text-align: center;
    font-weight: 600; font-size: 18px; letter-spacing: 1.2px; line-height: 1.35;
    white-space: nowrap;
  }
  .details__rule {
    margin: 7px auto 7px; width: 166px; border-top: 2px dashed var(--rule);
  }
</style>
</head>
<body>
  <div class="label">
    <div class="rule rule--top-left"></div>
    <div class="rule rule--top-right"></div>

    <div class="brand">Velka Botanix</div>
    <div class="slogan">NATURE’S RITUALS</div>

    <div class="product-name">TUMERIC AND NEEM SCRUB</div>
    <div class="product-rule"></div>

    <svg class="badges" width="210" height="72" viewBox="0 0 210 72" role="img" aria-label="Product certification badges">
      <circle cx="28" cy="38" r="26" fill="none" stroke="#2a2a2a" stroke-width="2.5"/>
      <circle cx="100" cy="33" r="26" fill="none" stroke="#2a2a2a" stroke-width="2.5"/>
      <circle cx="174" cy="36" r="26" fill="none" stroke="#2a2a2a" stroke-width="2.5"/>
    </svg>

    <div class="details">
      <div>ALL NATURAL<br>INGREDIENTS</div>
      <div class="details__rule"></div>
      <div>8OZ</div>
    </div>

    <div class="rule rule--bottom-thin"></div>
    <div class="rule rule--bottom-thick"></div>
  </div>
</body>
</html>
```